Job Coaching - Vanta; engaging people to improve their work experience

I need a flyer for Job Coaching. It serves to engage customers (not businesses) with problems in their daily job, typical questions that are handled are:
Do I fit for the job?
Am I using my talents at best in this job?
I have a conflict with my manager/colleagues, what should I do?
My work-life balance is a mess, how can I improve this?
What job fits best with my talents?
I'm getting stressed out from my job, what can I do?
....
This Flyer will be available at GP's, therpeutic practices, pharamcists,...
this flyer should put people in action to contact me
Flyer can be created in English, in the final one the text should be in Dutch; I will make the translation of the selected flyer and provide it at the end

Target Market(s)

consumers / customers / people having a job, but somewhat stuck in it

Industry/Entity Type

Professional Coaching

Requirements
Must have
• the questions mentioned in the project description; mobile number: 0471/389145; email: tom.vermeer@vantacoaching.example; website: www.vantacoaching.example ; it should make also reference to 'Career guidance cheques of the KWOL'

```html
<!DOCTYPE html>
<html lang="en">
<head>
<meta charset="utf-8">
<title>Vanta – Career Guidance Flyer</title>
<link href="https://fonts.googleapis.com/css2?family=Montserrat:wght@400;500;600;700&family=Oswald:wght@300;400;500;600&display=swap" rel="stylesheet">
<style>
:root{
  --teal:#2fb8a6;
  --teal-bright:#4fd6c8;
  --teal-deep:#1a8a7e;
  --teal-dark:#136b62;
  --ink:#2b2b2b;
  --charcoal:#333436;
  --grey-mid:#8a8b8d;
  --white:#ffffff;
}
*{margin:0;padding:0;box-sizing:border-box}
html,body{width:701px;height:1200px;overflow:hidden;background:#fff}
.flyer{position:relative;width:701px;height:1200px;overflow:hidden;font-family:"Montserrat",sans-serif;color:var(--white)}
.backdrop{position:absolute;inset:0}
.abs{position:absolute}
.photo-scene{position:absolute;left:370px;top:0;width:331px;height:560px;background:linear-gradient(160deg,#9c9d9f 0%,#6f7072 45%,#8b8c8e 100%);opacity:.55}

.brand{left:26px;top:42px;display:flex;align-items:center;gap:14px}
.brand-dot{width:78px;height:78px;border-radius:50%;background:var(--teal)}
.brand-name{font-weight:700;font-size:62px;color:var(--teal);letter-spacing:2px;line-height:1}
.brand-tag{left:118px;top:112px;font-size:15px;font-weight:500;color:var(--grey-mid)}

.title-career{left:26px;top:192px;font-size:64px;font-weight:400;letter-spacing:2px;line-height:1;color:var(--white)}
.title-guidance{left:26px;top:256px;font-size:38px;font-weight:700;line-height:1;color:var(--ink)}
.cheques{left:390px;top:202px;line-height:1.05}
.cheques-line1{font-size:20px;font-weight:600}
.cheques-line2{font-family:"Oswald",sans-serif;font-size:20px;font-weight:400}
.vouchers{left:382px;top:289px;font-size:17px;font-weight:600;font-style:italic;color:var(--ink);letter-spacing:.5px}

.intro{left:30px;top:347px;width:645px;list-style:none}
.intro li{position:relative;padding-left:22px;font-size:11px;line-height:1.38;margin-bottom:17px}
.intro li::before{content:"";position:absolute;left:0;top:1px;width:14px;height:14px;border-radius:50%;background:var(--teal-bright)}
.intro li::after{content:"";position:absolute;left:4px;top:4px;width:5px;height:3px;border-left:2px solid #fff;border-bottom:2px solid #fff;transform:rotate(-45deg)}

.counsel{left:48px;top:613px;font-family:"Oswald",sans-serif;font-size:27px;line-height:1.1;font-weight:300;transform:skewX(-8deg)}
.counsel b{font-weight:600}
.counsel .hl{color:var(--teal-bright);font-weight:600}
.situation{left:98px;top:702px;font-family:"Oswald",sans-serif;font-size:24px;line-height:1.3;font-weight:400;color:#5a5b5d}
.situation .hl{color:var(--teal-deep);font-weight:500}

.portrait{position:absolute;left:455px;top:640px;width:350px;height:350px;border-radius:50%;background:radial-gradient(circle at 45% 60%,#2a9a90 0%,#c9b2a2 55%,#f4f4f4 75%)}

.questions-head{left:46px;top:862px;font-family:"Oswald",sans-serif;font-size:21px;line-height:1.2;font-weight:300}
.questions-head b{color:var(--teal-bright);font-weight:500}
.questions{left:64px;top:922px;font-family:"Oswald",sans-serif;font-size:12.5px;line-height:1.5;font-weight:400;list-style:none;padding-left:8px;border-left:1px solid rgba(255,255,255,.6);text-transform:uppercase}

.together{left:175px;top:1050px;font-family:"Oswald",sans-serif;font-size:21px;font-weight:300}
.together b{font-weight:500}

.phone{left:22px;top:1119px;display:flex;align-items:center;gap:14px}
.phone-number{font-family:"Oswald",sans-serif;font-size:36px;font-weight:500}
.contacts{left:286px;top:1133px;display:flex;align-items:center;gap:8px}
.contact{display:flex;align-items:center;gap:4px;font-size:9.5px;font-weight:600;color:var(--ink);white-space:nowrap}
.contact .web-accent{color:var(--teal-deep)}
</style>
</head>
<body>
<main class="flyer">
  <svg class="backdrop" width="701" height="1200" viewBox="0 0 701 1200" aria-hidden="true">
    <defs>
      <linearGradient id="body-grey" x1="0" y1="0" x2="1" y2="0">
        <stop offset="0" stop-color="#6c6d6f"/><stop offset="1" stop-color="#a3a4a6"/>
      </linearGradient>
      <linearGradient id="band-teal" x1="0" y1="0" x2="1" y2="0">
        <stop offset="0" stop-color="#27ad9c"/><stop offset="1" stop-color="#4fd0c2"/>
      </linearGradient>
      <linearGradient id="lower-teal" x1="0" y1="0" x2="1" y2="1">
        <stop offset="0" stop-color="#35bfae"/><stop offset="1" stop-color="#1b8c80"/>
      </linearGradient>
      <linearGradient id="light-box" x1="0" y1="0" x2="1" y2="0">
        <stop offset="0" stop-color="#d8d9da"/><stop offset="1" stop-color="#ffffff"/>
      </linearGradient>
    </defs>
    <rect width="701" height="1200" fill="url(#body-grey)"/>
    <rect y="565" width="701" height="270" fill="#3a3b3d"/>
    <path d="M0 0 H490 C420 40 420 160 330 162 H0 Z" fill="#fff"/>
    <rect y="187" width="701" height="120" fill="url(#band-teal)"/>
    <path d="M345 329 L370 274 H701 V329 Z" fill="#e4e5e6"/>
    <path d="M0 560 C200 520 430 530 701 560 V565 H0 Z" fill="#3a3b3d"/>
    <path d="M78 692 H440 V830 H64 Z" fill="url(#light-box)"/>
    <path d="M0 830 L80 800 H701 V1085 H0 Z" fill="url(#lower-teal)"/>
    <path d="M0 800 L64 780 L80 830 L0 860 Z" fill="#2f3032"/>
    <path d="M150 1045 H701 V1085 H150 Q140 1065 150 1045 Z" fill="var(--teal-dark)"/>
    <rect y="1085" width="701" height="115" fill="#fff"/>
    <path d="M0 1085 H268 L300 1200 H0 Z" fill="var(--charcoal)"/>
    <circle cx="630" cy="815" r="190" fill="#fff"/>
    <path d="M462 725 A190 190 0 0 1 701 638" fill="none" stroke="var(--teal)" stroke-width="8"/>
  </svg>

  <div class="photo-scene" role="img" aria-label="Greyscale photo of a stressed man at an office desk with his hand to his head"></div>

  <div class="abs brand"><span class="brand-dot"></span><span class="brand-name">Vanta</span></div>
  <div class="abs brand-tag">professional coaching</div>

  <h1 class="abs title-career">CAREER</h1>
  <div class="abs title-guidance">GUIDANCE</div>
  <div class="abs cheques">
    <div class="cheques-line1">KWOL career cheques</div>
    <div class="cheques-line2">THESE CAN BE USED.</div>
  </div>
  <div class="abs vouchers">WITH CAREER VOUCHERS)</div>

  <ul class="abs intro">
    <li>We easily spend 8 hours a day on our professional pursuits, our job. If we assume that we sleep about 8 hours a day, that's 50% of our active time. We actually spend more time with our colleagues than with our partner and/or children.</li>
    <li>In addition, if things are not going well during those 8 hours, it also impacts the other 8 waking hours. If we don't feel good about ourselves at work, our family members, friends and acquaintances feel it too.</li>
    <li>So we'd better make sure that we spend those 8 hours meaningfully and, at best, get energy from it too. That we can accomplish a piece of our personal accomplishments there.</li>
    <li>Unfortunately, not every career goes smoothly, and it is even very normal that there are ups and downs this, nowadays more than 40-year career. But we can strive to keep these downs as short as possible and the ups as long as possible.</li>
  </ul>

  <div class="abs counsel">AND THAT'S WHERE <span class="hl">CAREER COUNSELING</span><br><b>COMES INTO PLAY</b></div>
  <div class="abs situation">DURING THIS CAREER COUNSELING,<br>WE TAKE A CLOSE LOOK AT YOUR<br><span class="hl">PERSONAL SITUATION...</span></div>

  <div class="portrait" role="img" aria-label="Portrait photo of the coach in a teal shirt"></div>

  <div class="abs questions-head">DO YOU RECOGNIZE YOURSELF IN ANY OF THE<br><b>FOLLOWING QUESTIONS?</b></div>
  <ol class="abs questions">
    <li>1. How can I get more energy from my job?</li>
    <li>2. How can I get a better work-life balance?</li>
    <li>3. What are my talents?</li>
    <li>4. How can I work better with my manager and/or colleagues?</li>
    <li>5. Do you know what you want, but do not dare to take the step?</li>
    <li>6. Or maybe you think you have more up your sleeve than you do today?</li>
  </ol>

  <div class="abs together">THEN WE WILL <b>WORK ON THIS TOGETHER.</b></div>

  <div class="abs phone">
    <svg width="46" height="46" viewBox="0 0 48 48" aria-hidden="true">
      <circle cx="24" cy="24" r="22" fill="var(--teal)" stroke="#fff" stroke-width="3"/>
      <path d="M17 14 l5 0 l2 6 l-3 2 q2 5 6 7 l2 -3 l6 2 l0 5 q-1 2 -3 2 q-16 -2 -17 -18 q0 -2 2 -3 z" fill="#fff"/>
    </svg>
    <span class="phone-number">0471/389145</span>
  </div>

  <div class="abs contacts">
    <div class="contact">
      <svg width="18" height="18" viewBox="0 0 20 20" aria-hidden="true"><circle cx="10" cy="10" r="9" fill="none" stroke="var(--teal)" stroke-width="1.5"/><rect x="5" y="6.5" width="10" height="7" fill="none" stroke="var(--teal)" stroke-width="1.2"/><path d="M5 6.5 L10 10.5 L15 6.5" fill="none" stroke="var(--teal)" stroke-width="1.2"/></svg>
      <span>tom.vermeer@vantacoaching.example</span>
    </div>
    <div class="contact">
      <svg width="18" height="18" viewBox="0 0 20 20" aria-hidden="true"><circle cx="10" cy="10" r="8" fill="none" stroke="var(--teal)" stroke-width="1.3"/><ellipse cx="10" cy="10" rx="3.5" ry="8" fill="none" stroke="var(--teal)" stroke-width="1.1"/><path d="M2 10 H18" stroke="var(--teal)" stroke-width="1.1"/></svg>
      <span>www.<span class="web-accent">vantacoaching</span>.example</span>
    </div>
  </div>
</main>
</body>
</html>
```